Working Capital graphics

Our business advisory firm requires 9 images to be re-created and improved in the branding of our business.

The 9 images have been uploaded below and the colours and branding of the business can be found at the website www.thornwickadvisory.com.au

```html
<!DOCTYPE html>
<html lang="en">
<head>
<meta charset="utf-8">
<title>Working Capital Graphics – Thornwick Advisory</title>
<link href="https://fonts.googleapis.com/css2?family=Lato:ital,wght@0,400;0,700;0,900;1,700;1,900&display=swap" rel="stylesheet">
<style>
  :root{
    --navy:#0d2240;
    --blue:#1ab0e8;
    --blue-dark:#0596cf;
    --blue-mid:#00aeea;
    --blue-light:#47ccf7;
    --blue-pale:#8ddcf8;
    --orange:#f7941d;
    --orange-dark:#ee8107;
    --orange-light:#fdb462;
    --frame:#cfcfcf;
    --white:#ffffff;
  }
  html,body{margin:0;padding:0;background:var(--white);overflow:hidden;}
  .canvas{width:1200px;height:1000px;overflow:hidden;}
  .canvas svg{display:block;width:1200px;height:1000px;}
  text{font-family:'Lato',sans-serif;}
  .panel-frame{fill:var(--white);stroke:var(--frame);stroke-width:1.5;}
  .node{fill:var(--white);stroke:var(--blue);stroke-width:2.5;}
  .node-label{font-weight:700;font-size:21px;letter-spacing:1.5px;fill:var(--navy);text-anchor:middle;}
  .hub{fill:var(--white);stroke:var(--orange);stroke-width:6;}
  .hub-label{font-weight:900;font-size:42px;letter-spacing:2px;fill:var(--navy);text-anchor:middle;}
  .ring{fill:none;stroke:var(--orange);stroke-width:2.5;}
  .panel-title{font-weight:900;font-style:italic;font-size:34px;letter-spacing:2px;fill:var(--navy);}
  .axis{stroke:var(--orange);stroke-width:3;fill:none;}
  .axis-tick{font-weight:700;font-size:21px;letter-spacing:1px;fill:var(--navy);}
  .axis-title{font-weight:700;font-size:22px;letter-spacing:2px;fill:var(--navy);}
  .guide{stroke:var(--navy);stroke-width:2.5;stroke-dasharray:9 7;fill:none;}
  .vector{stroke:var(--navy);stroke-width:2.5;fill:none;}
  .vector-letter{font-weight:700;font-size:46px;fill:var(--orange);}
  .vector-label{font-weight:700;font-size:22px;letter-spacing:2px;fill:var(--navy);}
  .col-head{font-weight:700;font-style:italic;font-size:20px;letter-spacing:1.5px;fill:var(--navy);text-anchor:middle;}
  .tree{stroke:var(--blue);stroke-width:2.5;fill:none;}
  .tree-orange{stroke:var(--orange);stroke-width:2.5;fill:none;}
  .root-box{fill:var(--white);stroke:var(--blue);stroke-width:3;}
  .root-label{font-weight:700;font-style:italic;font-size:21px;letter-spacing:1.5px;fill:var(--navy);text-anchor:middle;}
  .group-box{fill:var(--white);stroke:var(--orange);stroke-width:2.5;}
  .group-badge{fill:var(--orange);}
  .group-num{font-weight:700;font-size:25px;fill:var(--white);text-anchor:middle;}
  .group-label{font-weight:700;font-size:16px;letter-spacing:1.5px;fill:var(--navy);}
  .item-box{fill:var(--white);stroke:var(--blue);stroke-width:2.5;}
  .item-label{font-weight:700;font-size:15px;letter-spacing:1.5px;fill:var(--navy);}
  .seg-text{font-weight:900;font-size:15px;letter-spacing:.5px;fill:var(--white);text-anchor:middle;}
  .center-ring{fill:var(--white);stroke:var(--blue);stroke-width:3;}
  .center-label{font-weight:900;font-style:italic;font-size:32px;letter-spacing:1.5px;fill:var(--navy);text-anchor:middle;}
  .milestone{font-weight:700;font-size:15px;letter-spacing:1px;fill:var(--navy);text-anchor:middle;}
  .flag-pole{stroke:var(--blue);stroke-width:2.5;}
  .flag-cloth{fill:var(--white);stroke:var(--orange);stroke-width:2.5;}
  .brand-dot{fill:var(--blue);}
  .brand-name{font-weight:400;font-size:19px;letter-spacing:1px;fill:var(--blue);}
</style>
</head>
<body>
<div class="canvas">
<svg viewBox="0 0 2100 1760" preserveAspectRatio="xMidYMid meet" xmlns="http://www.w3.org/2000/svg">
  <defs>
    <marker id="arrowhead" viewBox="0 0 10 10" refX="8" refY="5" markerWidth="7" markerHeight="7" orient="auto-start-reverse">
      <path d="M0,0 L10,5 L0,10 Z" fill="var(--navy)"/>
    </marker>
    <linearGradient id="quadrantFill" x1="0" y1="0" x2="1" y2="1">
      <stop offset="0" stop-color="#c9eefc"/>
      <stop offset="1" stop-color="#00aeea"/>
    </linearGradient>
  </defs>

  <!-- Working capital drivers wheel -->
  <g class="panel panel-drivers">
    <rect class="panel-frame" x="163" y="22" width="852" height="853"/>
    <ellipse class="ring" cx="592" cy="442" rx="305" ry="300"/>
    <circle class="hub" cx="592" cy="452" r="140"/>
    <text class="hub-label"><tspan x="592" y="445">WORKING</tspan><tspan x="592" y="490">CAPITAL</tspan></text>

    <circle class="node" cx="590" cy="144" r="87"/>
    <text class="node-label"><tspan x="590" y="127">SUPPLY</tspan><tspan x="590" y="151">CHAIN</tspan><tspan x="590" y="175">ISSUES</tspan></text>
    <circle class="node" cx="398" cy="211" r="87"/>
    <text class="node-label"><tspan x="398" y="207">TERMS AND</tspan><tspan x="398" y="231">CONDITIONS</tspan></text>
    <circle class="node" cx="783" cy="211" r="87"/>
    <text class="node-label"><tspan x="783" y="207">PROCESS</tspan><tspan x="783" y="231">ISSUES</tspan></text>
    <circle class="node" cx="288" cy="394" r="87"/>
    <text class="node-label"><tspan x="288" y="378">IT SYSTEMS</tspan><tspan x="288" y="402">AND</tspan><tspan x="288" y="426">INFORMATION</tspan></text>
    <circle class="node" cx="894" cy="394" r="87"/>
    <text class="node-label"><tspan x="894" y="390">FORECASTING</tspan><tspan x="894" y="414">AND PLANNING</tspan></text>
    <circle class="node" cx="318" cy="597" r="87"/>
    <text class="node-label"><tspan x="318" y="593">KPIs AND</tspan><tspan x="318" y="617">MEASURES</tspan></text>
    <circle class="node" cx="862" cy="597" r="87"/>
    <text class="node-label"><tspan x="862" y="593">CUSTOMER</tspan><tspan x="862" y="617">MANAGEMENT</tspan></text>
    <circle class="node" cx="475" cy="739" r="87"/>
    <text class="node-label"><tspan x="475" y="735">SUPPLIER</tspan><tspan x="475" y="759">MANAGMENT</tspan></text>
    <circle class="node" cx="706" cy="739" r="87"/>
    <text class="node-label"><tspan x="706" y="735">SKU</tspan><tspan x="706" y="759">COMPLEXITY</tspan></text>

    <g class="brand">
      <circle class="brand-dot" cx="215" cy="808" r="16"/>
      <text class="brand-name" x="240" y="815">Thornwick Advisory</text>
    </g>
  </g>

  <!-- Net working capital absorption chart -->
  <g class="panel panel-absorption">
    <rect class="panel-frame" x="1085" y="22" width="852" height="853"/>
    <text class="panel-title" x="1150" y="95">NET WORKING CAPITAL ABSORPTION</text>

    <path d="M1533,414 L1533,252 A162,162 0 1 0 1695,414 Z" fill="url(#quadrantFill)" stroke="var(--blue)" stroke-width="2"/>
    <path class="guide" d="M1273,414 H1533 M1533,414 V683"/>
    <path class="axis" d="M1271,158 V683 H1787"/>

    <g class="axis-tick" text-anchor="end">
      <text x="1253" y="184">450m</text><text x="1253" y="253">400m</text><text x="1253" y="321">350m</text>
      <text x="1253" y="390">300m</text><text x="1253" y="458">250m</text><text x="1253" y="527">200m</text>
      <text x="1253" y="596">150m</text><text x="1253" y="664">100m</text>
    </g>
    <g class="axis-tick" text-anchor="middle">
      <text x="1318" y="716">20m</text><text x="1401" y="716">25m</text><text x="1484" y="716">30m</text>
      <text x="1567" y="716">35m</text><text x="1650" y="716">40m</text><text x="1733" y="716">45m</text>
    </g>
    <text class="axis-title" transform="translate(1168,420) rotate(-90)" text-anchor="middle">SALES</text>
    <text class="axis-title" x="1528" y="755" text-anchor="middle">NET WORKING CAPITAL (NWC)</text>

    <g marker-end="url(#arrowhead)">
      <line class="vector" x1="1533" y1="414" x2="1424" y2="256"/>
      <line class="vector" x1="1533" y1="414" x2="1533" y2="210"/>
      <line class="vector" x1="1533" y1="414" x2="1644" y2="256"/>
      <line class="vector" x1="1533" y1="414" x2="1728" y2="414"/>
      <line class="vector" x1="1533" y1="414" x2="1644" y2="574"/>
      <line class="vector" x1="1533" y1="414" x2="1424" y2="574"/>
    </g>
    <circle cx="1533" cy="414" r="12" fill="var(--navy)"/>

    <text class="vector-letter" x="1403" y="250">A</text>
    <text class="vector-label"><tspan x="1292" y="228">OPTIMAL</tspan><tspan x="1292" y="255">GROWTH</tspan></text>
    <text class="vector-letter" x="1518" y="204">B</text>
    <text class="vector-letter" x="1642" y="250">C</text>
    <text class="vector-label"><tspan x="1680" y="228">EASY</tspan><tspan x="1680" y="255">GROWTH</tspan></text>
    <text class="vector-letter" x="1732" y="430">D</text>
    <text class="vector-label"><tspan x="1769" y="408">DECLINING</tspan><tspan x="1769" y="434">GROWTH</tspan></text>
    <text class="vector-letter" x="1645" y="615">E</text>
    <text class="vector-label"><tspan x="1682" y="593">CORPORATE</tspan><tspan x="1682" y="619">STRESS</tspan></text>
    <text class="vector-letter" x="1402" y="615">F</text>
    <text class="vector-label" x="1417" y="635" text-anchor="middle">DOWNSIZING</text>

    <g class="brand">
      <circle class="brand-dot" cx="1150" cy="792" r="16"/>
      <text class="brand-name" x="1175" y="799">Thornwick Advisory</text>
    </g>
  </g>

  <!-- Inventory drivers tree -->
  <g class="panel panel-inventories">
    <rect class="panel-frame" x="163" y="875" width="852" height="853"/>
    <text class="panel-title" x="226" y="948">INVENTORIES</text>
    <text class="col-head" x="520" y="1022">DRIVER GROUP</text>
    <text class="col-head" x="828" y="1022">SUB-GROUP</text>

    <rect class="root-box" x="217" y="1306" width="145" height="87" rx="12"/>
    <text class="root-label"><tspan x="289" y="1347">INVENTORY</tspan><tspan x="289" y="1372">DRIVERS</tspan></text>
    <path class="tree" d="M362,1350 H383 M383,1115 V1583 M383,1115 H420 M383,1271 H420 M383,1427 H420 M383,1583 H420"/>

    <path class="tree-orange" d="M605,1115 H648 M648,1054 V1181 M648,1054 H677 M648,1096 H677 M648,1138 H677 M648,1181 H677"/>
    <path class="tree-orange" d="M605,1271 H648 M648,1226 V1313 M648,1226 H677 M648,1271 H677 M648,1313 H677"/>
    <path class="tree-orange" d="M605,1427 H648 M648,1383 V1472 M648,1383 H677 M648,1427 H677 M648,1472 H677"/>
    <path class="tree-orange" d="M605,1583 H648 M648,1538 V1628 M648,1538 H677 M648,1583 H677 M648,1628 H677"/>

    <g class="driver-group">
      <rect class="group-box" x="420" y="1098" width="185" height="34" rx="6"/>
      <circle class="group-badge" cx="424" cy="1115" r="21"/>
      <text class="group-num" x="424" y="1124">10</text>
      <text class="group-label" x="454" y="1121">PLANNING</text>
    </g>
    <g class="driver-group">
      <rect class="group-box" x="420" y="1254" width="185" height="34" rx="6"/>
      <circle class="group-badge" cx="424" cy="1271" r="21"/>
      <text class="group-num" x="424" y="1280">11</text>
      <text class="group-label" x="454" y="1277">PROCUREMENT</text>
    </g>
    <g class="driver-group">
      <rect class="group-box" x="420" y="1410" width="185" height="34" rx="6"/>
      <circle class="group-badge" cx="424" cy="1427" r="21"/>
      <text class="group-num" x="424" y="1436">12</text>
      <text class="group-label" x="454" y="1433">FULFILMENT</text>
    </g>
    <g class="driver-group">
      <rect class="group-box" x="420" y="1566" width="185" height="34" rx="6"/>
      <circle class="group-badge" cx="424" cy="1583" r="21"/>
      <text class="group-num" x="424" y="1592">13</text>
      <text class="group-label" x="454" y="1589">PRODUCT RANGE</text>
    </g>

    <g class="sub-groups">
      <rect class="item-box" x="677" y="1040" width="296" height="28" rx="5"/><text class="item-label" x="684" y="1059">DEMAND VARIABILITY</text>
      <rect class="item-box" x="677" y="1082" width="296" height="28" rx="5"/><text class="item-label" x="684" y="1101">PLANNING COLLABORATION</text>
      <rect class="item-box" x="677" y="1124" width="296" height="28" rx="5"/><text class="item-label" x="684" y="1143">INFORMATION AVAILABILITY</text>
      <rect class="item-box" x="677" y="1167" width="296" height="28" rx="5"/><text class="item-label" x="684" y="1186">INVENTORY TARGET SETTING</text>
      <rect class="item-box" x="677" y="1212" width="296" height="28" rx="5"/><text class="item-label" x="684" y="1231">ORDER QUANTITIES</text>
      <rect class="item-box" x="677" y="1257" width="296" height="28" rx="5"/><text class="item-label" x="684" y="1276">SUPPLIER LEAD TIME VARIABILITY</text>
      <rect class="item-box" x="677" y="1299" width="296" height="28" rx="5"/><text class="item-label" x="684" y="1318">SUPPLIER QUALITY VARIABILITY</text>
      <rect class="item-box" x="677" y="1369" width="296" height="28" rx="5"/><text class="item-label" x="684" y="1388">CUSTOMER SERVICE LEVELS</text>
      <rect class="item-box" x="677" y="1413" width="296" height="28" rx="5"/><text class="item-label" x="684" y="1432">NETWORK STRUCTURE</text>
      <rect class="item-box" x="677" y="1458" width="296" height="28" rx="5"/><text class="item-label" x="684" y="1477">INVENTORY POSTPONEMENT</text>
      <rect class="item-box" x="677" y="1524" width="296" height="28" rx="5"/><text class="item-label" x="684" y="1543">CUSTOMER INVENTORY NEEDS</text>
      <rect class="item-box" x="677" y="1569" width="296" height="28" rx="5"/><text class="item-label" x="684" y="1588">PART STANDARDISATION</text>
      <rect class="item-box" x="677" y="1614" width="296" height="28" rx="5"/><text class="item-label" x="684" y="1633">SKU PROLIFERATION</text>
    </g>

    <g class="brand">
      <circle class="brand-dot" cx="222" cy="1643" r="16"/>
      <text class="brand-name" x="247" y="1650">Thornwick Advisory</text>
    </g>
  </g>

  <!-- Next $100 of sales cycle -->
  <g class="panel panel-sales-cycle">
    <rect class="panel-frame" x="1085" y="875" width="852" height="853"/>

    <path d="M1432.4,976.1 A300,300 0 0 1 1576.8,961.0 L1561.7,1067.9 A192,192 0 0 0 1469.3,1077.5 Z" fill="var(--blue-mid)"/>
    <path d="M1576.8,961.0 A300,300 0 0 1 1816.9,1155.4 L1715.4,1192.3 A192,192 0 0 0 1561.7,1067.9 Z" fill="var(--blue-light)"/>
    <path d="M1816.9,1155.4 A300,300 0 0 1 1764.8,1450.8 L1682.1,1381.4 A192,192 0 0 0 1715.4,1192.3 Z" fill="var(--blue-pale)"/>
    <path d="M1764.8,1450.8 A300,300 0 0 1 1508.9,1556.9 L1518.3,1449.3 A192,192 0 0 0 1682.1,1381.4 Z" fill="var(--orange-dark)"/>
    <path d="M1508.9,1556.9 A300,300 0 0 1 1253.1,1360.6 L1354.6,1323.7 A192,192 0 0 0 1518.3,1449.3 Z" fill="var(--orange)"/>
    <path d="M1253.1,1360.6 A300,300 0 0 1 1342.2,1028.2 L1411.6,1110.9 A192,192 0 0 0 1354.6,1323.7 Z" fill="var(--orange-light)"/>
    <path d="M1342.2,1028.2 A300,300 0 0 1 1432.4,976.1 L1469.3,1077.5 A192,192 0 0 0 1411.6,1110.9 Z" fill="var(--blue-dark)"/>

    <circle class="center-ring" cx="1535" cy="1258" r="162"/>
    <text class="center-label"><tspan x="1535" y="1253">NEXT $100 OF</tspan><tspan x="1535" y="1292">SALES VOLUME</tspan></text>

    <text class="seg-text" x="1501" y="1028">$0</text>
    <text class="seg-text"><tspan x="1383" y="1053">CASH</tspan><tspan x="1383" y="1071">SHORTFALL</tspan></text>
    <text class="seg-text" x="1655" y="1057">COST OF SALES</text>
    <text class="seg-text"><tspan x="1777" y="1219">OPERATING</tspan><tspan x="1777" y="1237">EXPENSES</tspan></text>
    <text class="seg-text"><tspan x="1766" y="1327">FIXED</tspan><tspan x="1766" y="1345">COSTS</tspan></text>
    <text class="seg-text" x="1695" y="1443">TAX</text>
    <text class="seg-text" x="1656" y="1480">INTEREST</text>
    <text class="seg-text" x="1587" y="1512">DIVIDENDS</text>
    <text class="seg-text"><tspan x="1335" y="1399">AR</tspan><tspan x="1335" y="1417">DAYS</tspan></text>
    <text class="seg-text"><tspan x="1392" y="1459">AP</tspan><tspan x="1392" y="1477">DAYS</tspan></text>
    <text class="seg-text"><tspan x="1467" y="1498">INV</tspan><tspan x="1467" y="1516">DAYS</tspan></text>
    <text class="seg-text"><tspan x="1290" y="1247">ADDITIONAL</tspan><tspan x="1290" y="1263">DEBT</tspan></text>

    <text class="milestone" x="1529" y="942">REVENUE $0</text>
    <text class="milestone"><tspan x="1838" y="1089">GROSS</tspan><tspan x="1838" y="1107">MARGIN</tspan><tspan x="1838" y="1125">$0</tspan></text>
    <text class="milestone"><tspan x="1834" y="1417">EBIT</tspan><tspan x="1834" y="1435">$0</tspan></text>
    <text class="milestone"><tspan x="1530" y="1593">RETAINED</tspan><tspan x="1530" y="1612">INCOME</tspan><tspan x="1530" y="1631">$0</tspan></text>
    <text class="milestone"><tspan x="1216" y="1391">AFTER</tspan><tspan x="1216" y="1410">WORKING</tspan><tspan x="1216" y="1429">CAPITAL</tspan><tspan x="1216" y="1448">$0</tspan></text>
    <text class="milestone"><tspan x="1213" y="1077">AFTER</tspan><tspan x="1213" y="1096">ADDITIONAL</tspan><tspan x="1213" y="1115">FUNDING</tspan><tspan x="1213" y="1134">$0</tspan></text>

    <g class="flag"><line class="flag-pole" x1="1124" y1="1086" x2="1136" y2="1122"/><path class="flag-cloth" d="M1127,1088 Q1140,1080 1150,1086 Q1155,1082 1154,1094 Q1144,1100 1132,1102 Z"/></g>
    <g class="flag"><line class="flag-pole" x1="1873" y1="1086" x2="1885" y2="1122"/><path class="flag-cloth" d="M1876,1088 Q1889,1080 1899,1086 Q1904,1082 1903,1094 Q1893,1100 1881,1102 Z"/></g>
    <g class="flag"><line class="flag-pole" x1="1858" y1="1401" x2="1870" y2="1437"/><path class="flag-cloth" d="M1861,1403 Q1874,1395 1884,1401 Q1889,1397 1888,1409 Q1878,1415 1866,1417 Z"/></g>
    <g class="flag"><line class="flag-pole" x1="1580" y1="1592" x2="1592" y2="1628"/><path class="flag-cloth" d="M1583,1594 Q1596,1586 1606,1592 Q1611,1588 1610,1600 Q1600,1606 1588,1608 Z"/></g>
    <g class="flag"><line class="flag-pole" x1="1138" y1="1400" x2="1150" y2="1436"/><path class="flag-cloth" d="M1141,1402 Q1154,1394 1164,1400 Q1169,1396 1168,1408 Q1158,1414 1146,1416 Z"/></g>

    <g class="brand">
      <circle class="brand-dot" cx="1139" cy="1640" r="16"/>
      <text class="brand-name" x="1164" y="1647">Thornwick Advisory</text>
    </g>
  </g>
</svg>
</div>
</body>
</html>
```